KORVa: AI driven decarbonization application

We are seeking an engaging, user-friendly, and visually appealing user interface for our B2B SaaS platform, Brelmont KORVa. This solution helps large organizations achieve net-zero emissions using AI-driven forecasting, AI models, a emission mitigation library, and a scenario simulator..

A big challenge is to allow the user to work efficiently with multidimensional data.

Requirements:

* Design a modern, professional, and visually striking user interface, catering to a diverse audience within large corporations, including executives, strategists, and environmental specialists.

* Construct an intuitive navigation system, allowing users to seamlessly access functionalities for informed decision-making and tracking progress towards net-zero emissions.

* The application is expected to be used on desktops first

* Incorporate our brand's colors, and visual elements into the design to maintain consistency throughout the application.

* Provide design assets and documentation, such as style guides, design specifications, and necessary assets (e.g., icons, illustrations) for our development team to implement the design. We use Figma and would appreciate delivery as figma files.

Please note that we also need more pages over time. The most important is to get the work bench page right. We will also need:
* a landing page where the users can select previous scenarios and see some high level data.
* A page with information on historical data per asset
* An analytics page
* User and system administration pages.
These pages are out of scope for this project, but they should be available in the navigation solution.

Please submit your initial design concepts, accompanied by a brief explanation of your approach and the rationale behind your design choices. We will offer feedback and collaborate with the chosen designer to refine the design, ensuring it meets our requirements and vision.

We are really hoping to see some elegant user interfaces. The functionality describe in the attachment is important, but the layout is not. Feel free to invent.

Attached files:

Target Market(s)

Energy intensive industries

Requirements
Must have
• Easy to navigate through the different data dimensions: Time, assets, mitigation measures, and advanced details under mitigation measures. The design in the attached files are just our working drafts. Creative alternatives are very welcome.
Nice to have
• Elegant layouts that differ from our working drafts.

```html
<!DOCTYPE html>
<html lang="en">
<head>
<meta charset="utf-8">
<title>Brelmont KORVa – Scenario Simulation</title>
<link rel="stylesheet" href="https://fonts.googleapis.com/css2?family=Saira:wght@400;500;600;700&display=swap">
<style>
  :root {
    --teal: #5b9a98;
    --teal-text: #4f8e90;
    --navy: #1a5d96;
    --bg-top: #135993;
    --bg-bottom: #2474b6;
    --row: rgba(255,255,255,0.09);
    --white: #ffffff;
    --axis: #e3e9ee;
    --chart-label: #4f8e90;
    --map-tone: #eef3f9;
  }
  * { box-sizing: border-box; margin: 0; padding: 0; }
  html, body { width: 1200px; height: 1072px; overflow: hidden; }
  body {
    font-family: "Saira", sans-serif;
    background: linear-gradient(180deg, var(--bg-top) 0%, var(--bg-bottom) 100%);
    position: relative;
    color: var(--white);
  }
  .topbar {
    position: absolute; left: 0; top: 0; width: 1200px; height: 52px;
    background: var(--white);
  }
  .brand {
    position: absolute; left: 58px; top: 11px;
    font-size: 22px; font-weight: 500; letter-spacing: 1.5px;
    color: var(--navy);
  }
  .nav { position: absolute; left: 0; top: 0; height: 52px; }
  .nav a {
    position: absolute; top: 18px; height: 34px; line-height: 36px;
    font-size: 14px; color: var(--teal-text); text-decoration: none;
    white-space: nowrap;
  }
  .nav .active {
    background: var(--teal); color: var(--white); font-weight: 600;
    border-radius: 7px 7px 0 0; padding: 0; text-align: center;
    font-size: 12.5px; letter-spacing: .2px;
  }
  .user { position: absolute; left: 1022px; top: 13px; line-height: 1; }
  .user-name { font-size: 13px; font-weight: 700; color: var(--navy); }
  .user-org { font-size: 8px; color: var(--teal-text); margin-top: 2px; }
  .avatar {
    position: absolute; left: 1106px; top: 9px; width: 34px; height: 34px;
    border-radius: 50%; border: 2px solid #d8e4ea; background: var(--white);
  }
  .sidebar { position: absolute; left: 58px; top: 0; width: 258px; }
  .sidebar-title {
    position: absolute; top: 102px; left: 0;
    font-size: 25px; font-weight: 700; white-space: nowrap;
  }
  .group-head {
    position: absolute; left: 0; width: 258px; height: 37px;
    background: var(--white); border-radius: 3px;
    color: var(--teal-text); font-size: 17px; font-weight: 700;
    line-height: 37px; padding-left: 9px; white-space: nowrap;
  }
  .group-head svg { position: absolute; right: 10px; top: 13px; }
  .option {
    position: absolute; left: 0; width: 258px; height: 37px;
    background: var(--row); border-radius: 2px;
    font-size: 13.5px; line-height: 37px; padding-left: 9px; white-space: nowrap;
  }
  .option svg { position: absolute; right: 12px; top: 13px; }
  .chart-card {
    position: absolute; left: 333px; top: 110px; width: 809px; height: 722px;
    background: var(--white); border-radius: 17px; overflow: hidden;
  }
</style>
</head>
<body>
  <header class="topbar">
    <div class="brand">BRELMONT</div>
    <nav class="nav">
      <a style="left:435px">Home</a>
      <a style="left:500px">Assets</a>
      <a class="active" style="left:554px;width:174px">SCENARIO SIMULATION</a>
      <a style="left:743px">Map</a>
    </nav>
    <div class="user">
      <div class="user-name">MARTIN</div>
      <div class="user-org">My Company</div>
    </div>
    <div class="avatar">
      <svg width="30" height="30" viewBox="0 0 30 30"><circle cx="15" cy="11" r="4.5" fill="#5b9a98"/><path d="M7 23 C7 16 23 16 23 23 Z" fill="#5b9a98"/></svg>
    </div>
  </header>

  <aside class="sidebar">
    <h1 class="sidebar-title">Scenario Tuning</h1>

    <div class="group-head" style="top:149px">Switch Energy Carrier<svg width="12" height="8" viewBox="0 0 12 8"><path d="M1 1 L6 6 L11 1" fill="none" stroke="#5b9a98" stroke-width="1.6"/></svg></div>
    <div class="option" style="top:191px">Switch Energy Carrier<svg width="11" height="11"><rect width="11" height="11" rx="1.5" fill="#fff"/><path d="M2.5 5.8 L4.6 7.8 L8.6 3.4" fill="none" stroke="#2569a3" stroke-width="1.6"/></svg></div>
    <div class="option" style="top:233px">Biodiesel<svg width="11" height="11"><rect width="11" height="11" rx="1.5" fill="#fff"/><path d="M2.5 5.8 L4.6 7.8 L8.6 3.4" fill="none" stroke="#2569a3" stroke-width="1.6"/></svg></div>
    <div class="option" style="top:274px">Ethanol<svg width="11" height="11"><rect width="11" height="11" rx="1.5" fill="#fff"/><path d="M2.5 5.8 L4.6 7.8 L8.6 3.4" fill="none" stroke="#2569a3" stroke-width="1.6"/></svg></div>
    <div class="option" style="top:316px">Hydrogen<svg width="11" height="11"><rect width="11" height="11" rx="1.5" fill="#fff"/><path d="M2.5 5.8 L4.6 7.8 L8.6 3.4" fill="none" stroke="#2569a3" stroke-width="1.6"/></svg></div>
    <div class="option" style="top:358px">Methanol<svg width="11" height="11"><rect width="11" height="11" rx="1.5" fill="#fff"/><path d="M2.5 5.8 L4.6 7.8 L8.6 3.4" fill="none" stroke="#2569a3" stroke-width="1.6"/></svg></div>
    <div class="option" style="top:399px">Power from offshore wind<svg width="11" height="11"><rect width="11" height="11" rx="1.5" fill="#fff"/><path d="M2.5 5.8 L4.6 7.8 L8.6 3.4" fill="none" stroke="#2569a3" stroke-width="1.6"/></svg></div>
    <div class="option" style="top:441px">Power form shore<svg width="11" height="11"><rect width="11" height="11" rx="1.5" fill="#fff"/><path d="M2.5 5.8 L4.6 7.8 L8.6 3.4" fill="none" stroke="#2569a3" stroke-width="1.6"/></svg></div>

    <div class="group-head" style="top:503px">Energy efficiency measures<svg width="12" height="8" viewBox="0 0 12 8"><path d="M1 1 L6 6 L11 1" fill="none" stroke="#5b9a98" stroke-width="1.6"/></svg></div>
    <div class="option" style="top:545px">Venting to flare<svg width="11" height="11"><rect width="11" height="11" rx="1.5" fill="#fff"/><path d="M2.5 5.8 L4.6 7.8 L8.6 3.4" fill="none" stroke="#2569a3" stroke-width="1.6"/></svg></div>
    <div class="option" style="top:587px">Venting to production<svg width="11" height="11"><rect width="11" height="11" rx="1.5" fill="#fff"/><path d="M2.5 5.8 L4.6 7.8 L8.6 3.4" fill="none" stroke="#2569a3" stroke-width="1.6"/></svg></div>
    <div class="option" style="top:628px">Fugitive emission measure<svg width="11" height="11"><rect width="11" height="11" rx="1.5" fill="#fff"/><path d="M2.5 5.8 L4.6 7.8 L8.6 3.4" fill="none" stroke="#2569a3" stroke-width="1.6"/></svg></div>
    <div class="option" style="top:670px">Compressor replacement<svg width="11" height="11"><rect width="11" height="11" rx="1.5" fill="#fff"/><path d="M2.5 5.8 L4.6 7.8 L8.6 3.4" fill="none" stroke="#2569a3" stroke-width="1.6"/></svg></div>
    <div class="option" style="top:712px">Reduced water injection<svg width="11" height="11"><rect width="11" height="11" rx="1.5" fill="#fff"/><path d="M2.5 5.8 L4.6 7.8 L8.6 3.4" fill="none" stroke="#2569a3" stroke-width="1.6"/></svg></div>
    <div class="option" style="top:753px">Reduced gas injection<svg width="11" height="11"><rect width="11" height="11" rx="1.5" fill="#fff"/><path d="M2.5 5.8 L4.6 7.8 L8.6 3.4" fill="none" stroke="#2569a3" stroke-width="1.6"/></svg></div>
    <div class="option" style="top:795px">Drilling improvements<svg width="11" height="11"><rect width="11" height="11" rx="1.5" fill="#fff"/><path d="M2.5 5.8 L4.6 7.8 L8.6 3.4" fill="none" stroke="#2569a3" stroke-width="1.6"/></svg></div>

    <div class="group-head" style="top:858px">Logistics<svg width="8" height="12" viewBox="0 0 8 12"><path d="M6 1 L1.5 6 L6 11" fill="none" stroke="#5b9a98" stroke-width="1.6"/></svg></div>
    <div class="group-head" style="top:901px">End of pipe measures<svg width="8" height="12" viewBox="0 0 8 12"><path d="M6 1 L1.5 6 L6 11" fill="none" stroke="#5b9a98" stroke-width="1.6"/></svg></div>
    <div class="group-head" style="top:944px">Carbon Offsets<svg width="8" height="12" viewBox="0 0 8 12"><path d="M6 1 L1.5 6 L6 11" fill="none" stroke="#5b9a98" stroke-width="1.6"/></svg></div>
    <div class="group-head" style="top:988px">Company Structure<svg width="8" height="12" viewBox="0 0 8 12"><path d="M6 1 L1.5 6 L6 11" fill="none" stroke="#5b9a98" stroke-width="1.6"/></svg></div>
  </aside>

  <section class="chart-card">
    <svg width="809" height="722" viewBox="0 0 970 866" font-family="Saira, sans-serif">
      <defs>
        <linearGradient id="map-fade" x1="0" y1="0" x2="0" y2="1">
          <stop offset="0" stop-color="#f1f5fa"/><stop offset="1" stop-color="#f6f9fc"/>
        </linearGradient>
        <linearGradient id="line-green" x1="90" y1="0" x2="922" y2="0" gradientUnits="userSpaceOnUse">
          <stop offset="0" stop-color="#78d86c"/><stop offset=".55" stop-color="#a9d563"/><stop offset="1" stop-color="#e3c65a"/>
        </linearGradient>
        <linearGradient id="line-purple" x1="90" y1="0" x2="922" y2="0" gradientUnits="userSpaceOnUse">
          <stop offset="0" stop-color="#98507f"/><stop offset=".5" stop-color="#a84aa8"/><stop offset="1" stop-color="#c84ee6"/>
        </linearGradient>
        <linearGradient id="line-blue" x1="90" y1="0" x2="922" y2="0" gradientUnits="userSpaceOnUse">
          <stop offset="0" stop-color="#5fd8f7"/><stop offset=".5" stop-color="#7aa8f2"/><stop offset="1" stop-color="#a98af0"/>
        </linearGradient>
      </defs>
      <rect x="110" y="178" width="860" height="530" rx="40" fill="url(#map-fade)" role="img" aria-label="Faint world map backdrop"/>
      <line x1="90" y1="38" x2="90" y2="790" stroke="var(--axis)" stroke-width="2"/>
      <line x1="90" y1="790" x2="945" y2="790" stroke="var(--axis)" stroke-width="2"/>
      <g fill="#4f8e90" font-size="15" font-weight="600">
        <text x="83" y="48" text-anchor="end">20</text>
        <text x="83" y="218" text-anchor="end">15</text>
        <text x="83" y="406" text-anchor="end">10</text>
        <text x="83" y="636" text-anchor="end">5</text>
        <text x="83" y="793" text-anchor="end">0</text>
        <text x="88" y="812">2010</text>
        <text x="299" y="812">2020</text>
        <text x="513" y="812">2030</text>
        <text x="727" y="812">2040</text>
        <text transform="translate(41 443) rotate(-90)" text-anchor="middle" font-size="16" font-weight="500">Relative Emissions, Kg CO2e / produced unit</text>
      </g>
      <text x="505" y="664" fill="#5b9a98" font-size="26" font-weight="600">Company Goal</text>
      <g fill="none" stroke-width="4" stroke-linecap="round">
        <path stroke="url(#line-blue)" d="M90 428 C127 402 127 402 165 402 C221 402 221 531 277 531 C323 531 323 334 370 334 C405 334 405 493 440 493 C477 493 477 357 515 357 C538 357 538 498 560 498 C603 498 603 408 645 408 C700 408 700 520 755 520 C838 520 838 408 922 408"/>
        <path stroke="url(#line-green)" d="M90 518 C130 580 140 621 170 621 C222 621 222 171 273 171 C322 171 322 606 370 606 C409 606 409 455 448 455 C482 455 482 621 515 621 C589 621 589 534 663 534 C792 534 792 590 922 590"/>
        <path stroke="url(#line-purple)" d="M90 401 C120 300 130 235 168 235 C220 235 220 623 273 623 C355 623 355 429 436 429 C549 429 549 565 662 565 C792 565 792 325 922 325"/>
      </g>
    </svg>
  </section>
</body>
</html>
```